Human Resources Flyer design

Create a 1 page flyer design for a staffing company that is looking to provide its services to clients. Images centered around people and businesses.
Target Market(s)
Large businesses
Industry/Entity Type
Staffing
Requirements
Must have
- Use color scheme that matches norvelhire.example.
Nice to have
- Flow chart like image for 3 areas mentioned.
- Images that convey professionalism and people connections

```html
<!DOCTYPE html>
<html lang="en">
<head>
<meta charset="utf-8">
<title>Norvel Hire – Staffing Flyer</title>
<link rel="stylesheet" href="https://fonts.googleapis.com/css2?family=Montserrat:wght@400;600;700;800&family=Open+Sans:ital,wght@0,400;0,600;1,400&display=swap">
<style>
  :root {
    --red: #c01f26;
    --red-dark: #9c161c;
    --slate: #5b6169;
    --slate-dark: #3b4047;
    --photo-top: #55606c;
    --photo-bottom: #8d97a1;
    --white: #ffffff;
    --ink: #3d3d3d;
    --stage: #e4e4e4;
  }
  * { box-sizing: border-box; margin: 0; padding: 0; }
  html, body { width: 880px; height: 1200px; overflow: hidden; background: var(--stage); }
  body { position: relative; font-family: "Open Sans", Arial, sans-serif; }
  .page {
    position: absolute; top: 303px; width: 420px; height: 594px;
    overflow: hidden; background: var(--white);
    box-shadow: 0 6px 18px rgba(0,0,0,.22);
  }
  .page--front { left: 15px; background: var(--red); }
  .page--back { left: 445px; }
  .page__shapes { position: absolute; inset: 0; }
  .brand {
    position: absolute; display: flex; align-items: center; gap: 7px;
    font-family: "Montserrat", Arial, sans-serif; font-weight: 800;
    font-size: 17px; letter-spacing: 1.5px; text-transform: uppercase;
  }
  .brand__mark { width: 10px; height: 10px; background: currentColor; }
  .front__brand { left: 24px; top: 30px; color: var(--white); }
  .front__headline {
    position: absolute; left: 24px; top: 236px;
    font-family: "Montserrat", Arial, sans-serif; font-weight: 700;
    font-size: 22px; color: var(--white);
  }
  .front__tagline { position: absolute; left: 24px; top: 268px; font-size: 8.5px; color: #f1d6d7; }
  .front__intro {
    position: absolute; left: 24px; top: 320px; width: 215px;
    font-size: 10.5px; line-height: 1.45; color: var(--white);
  }
  .front__quote {
    position: absolute; left: 24px; top: 410px; width: 215px;
    font-size: 10.5px; line-height: 1.45; font-style: italic; color: var(--white);
  }
  .front__web { position: absolute; left: 24px; bottom: 20px; font-size: 9px; font-weight: 600; color: var(--white); }

  .back__steps { position: absolute; top: 52px; left: 0; width: 420px; display: flex; justify-content: center; gap: 28px; }
  .step-label {
    width: 74px; height: 74px; display: flex; align-items: center; justify-content: center;
    text-align: center; font-family: "Montserrat", Arial, sans-serif; font-weight: 600;
    font-size: 8.5px; line-height: 1.2; color: var(--white);
  }
  .back__body { position: absolute; left: 26px; top: 186px; width: 368px; }
  .back__heading {
    font-family: "Montserrat", Arial, sans-serif; font-weight: 700;
    font-size: 13px; color: var(--red);
  }
  .back__intro { font-size: 9px; color: var(--ink); margin: 4px 0 14px; }
  .service { display: flex; gap: 10px; margin-bottom: 14px; }
  .service__icon {
    flex: none; width: 22px; height: 22px; background: var(--red);
    display: flex; align-items: center; justify-content: center;
  }
  .service__title {
    font-family: "Montserrat", Arial, sans-serif; font-weight: 700;
    font-size: 10.5px; color: var(--red); margin-bottom: 3px;
  }
  .service__text { font-size: 9px; line-height: 1.45; color: var(--ink); }
  .contact { position: absolute; left: 26px; bottom: 30px; font-size: 8.5px; color: var(--ink); line-height: 1.6; }
  .contact__title { font-family: "Montserrat", Arial, sans-serif; font-weight: 700; font-size: 10px; color: var(--red); }
  .back__brand { right: 26px; bottom: 34px; color: var(--red); font-size: 15px; }
</style>
</head>
<body>

<section class="page page--front">
  <svg class="page__shapes" viewBox="0 0 420 594" width="420" height="594">
    <defs>
      <linearGradient id="site-photo" x1="0" y1="0" x2="0" y2="1">
        <stop offset="0" stop-color="var(--photo-top)"/>
        <stop offset="1" stop-color="var(--photo-bottom)"/>
      </linearGradient>
    </defs>
    <g role="img" aria-label="Photo of construction workers on a building site">
      <polygon points="0,0 420,0 420,175 0,215" fill="url(#site-photo)"/>
    </g>
    <polygon points="300,0 420,0 420,110" fill="var(--red)"/>
    <polygon points="360,0 420,0 420,55" fill="var(--slate)"/>
    <polygon points="0,0 70,0 0,90" fill="var(--red-dark)" opacity=".85"/>
    <line x1="0" y1="215" x2="420" y2="175" stroke="var(--white)" stroke-width="5"/>
    <line x1="275" y1="594" x2="420" y2="330" stroke="var(--white)" stroke-width="6"/>
    <line x1="305" y1="594" x2="420" y2="385" stroke="var(--white)" stroke-width="2" opacity=".7"/>
    <polygon points="340,594 420,460 420,594" fill="var(--slate)"/>
  </svg>
  <div class="brand front__brand"><span class="brand__mark"></span>Norvel Hire</div>
  <h1 class="front__headline">Let Our Team Become Yours.</h1>
  <p class="front__tagline">A complete workforce solution for your business</p>
  <p class="front__intro">Norvel Hire combines the best tools in human resource and risk management with industry-leading knowledge to create a unique operational platform.</p>
  <p class="front__quote">“Our expertise in human resource management, risk mitigation and safety, payroll administration, workers’ compensation coverage and employee benefits allow our clients to focus on their core business.”</p>
  <p class="front__web">www.norvelhire.example</p>
</section>

<section class="page page--back">
  <svg class="page__shapes" viewBox="0 0 420 594" width="420" height="594">
    <polygon points="0,0 420,0 420,150 0,170" fill="var(--red)"/>
    <polygon points="0,0 90,0 0,70" fill="var(--slate)"/>
    <polygon points="340,0 420,0 420,60" fill="var(--red-dark)"/>
    <g fill="none" stroke="var(--white)" stroke-width="5">
      <circle cx="108" cy="89" r="40"/>
      <circle cx="210" cy="89" r="40"/>
      <circle cx="312" cy="89" r="40"/>
    </g>
    <g stroke="var(--white)" stroke-width="4">
      <line x1="148" y1="89" x2="170" y2="89"/>
      <line x1="250" y1="89" x2="272" y2="89"/>
    </g>
    <polygon points="0,594 0,576 48,594" fill="var(--red)"/>
    <polygon points="420,545 420,594 382,594" fill="var(--slate)" opacity=".25"/>
  </svg>

  <div class="back__steps">
    <div class="step-label">Tactical<br>Alignment</div>
    <div class="step-label">Expansion<br>Development</div>
    <div class="step-label">Business-level<br>guidance</div>
  </div>

  <div class="back__body">
    <h2 class="back__heading">What can we expect from Norvel Hire</h2>
    <p class="back__intro">Business success starts with the right people, guided through three clear stages.</p>

    <div class="service">
      <div class="service__icon"><svg width="12" height="12" viewBox="0 0 12 12"><polyline points="2,6 5,9 10,3" fill="none" stroke="#fff" stroke-width="2"/></svg></div>
      <div>
        <h3 class="service__title">Tactical Alignment</h3>
        <p class="service__text">We align your hiring plans with business goals so every role supports growth.</p>
      </div>
    </div>
    <div class="service">
      <div class="service__icon"><svg width="12" height="12" viewBox="0 0 12 12"><polyline points="2,6 5,9 10,3" fill="none" stroke="#fff" stroke-width="2"/></svg></div>
      <div>
        <h3 class="service__title">Expansion Development</h3>
        <p class="service__text">We scale teams quickly with vetted talent, payroll support and steady onboarding.</p>
      </div>
    </div>
    <div class="service">
      <div class="service__icon"><svg width="12" height="12" viewBox="0 0 12 12"><polyline points="2,6 5,9 10,3" fill="none" stroke="#fff" stroke-width="2"/></svg></div>
      <div>
        <h3 class="service__title">Business-level guidance</h3>
        <p class="service__text">Our advisors help leaders plan workforce needs, manage risk and keep teams productive.</p>
      </div>
    </div>
  </div>

  <div class="contact">
    <p class="contact__title">Contact Info</p>
    <p>+1 555 010 2040</p>
    <p>hello@norvelhire.example</p>
  </div>
  <div class="brand back__brand"><span class="brand__mark"></span>Norvel Hire</div>
</section>

</body>
</html>
```